Innovative Veterinary Clinic Business Card

We are a mixed animal veterinary practice in rural Queensland. Our patients include cattle, horses, dogs and cats, with everything in between. We are moving the clinic forward to become the best in our region and one of the best in the State, with gold standard service and standards of care, while remaining down to earth and genuine. Our current motto is - "Patients First, Every Visit". The clinic colours are blue and red but am open to change. I would like something innovative and modern, that stands out and says we are different, we are amazing, and our patients come first. Something that will be remembered. Our current logo and business card I feel are empty and don't stand out.
Updates

please use font that is strong but simple. I am looking for something different, rather than your run of the mill business card. I am open to anything - as long as it has two sides and defines us, I'll consider all submissions. Thank you for your efforts, they are all very much appreciated!!

Thank you all very much for your amazing efforts. I wasn't expecting to have such a great response, so I thank you for your participation. You are all very talented and I loved your designs. I wish you all the best for the future. Thank you!

Target Market(s)

pet owners, graziers, horse clients (horses of all types - pets, campdrafting, mustering, polocrosse, thoroughbreds, show ponies)

Industry/Entity Type

Veterinary

Contact Information for Business Card

Dr. Freya L Tovell - BVSc (Hons)
Creekbend Veterinary Services
17 Harrow St
Wattlegrove, QLD, 4626
Ph: 0741872306 or 0418365947
Fax: 0741872309
e: creekbendvets@mailnest.example

Colors

Designer to choose colors to be used in the design.

Requirements
Must have
• back side of card to be used as an appointment card
Nice to have
• perhaps a photo of an animal (horse, dog, cat, cattle)
Should not have
• I don't want the standard name, rank and serial number business card. No cartoon animals.

```html
<!DOCTYPE html>
<html lang="en">
<head>
<meta charset="utf-8">
<title>Creekbend Veterinary Services – Business & Appointment Card</title>
<link rel="stylesheet" href="https://fonts.googleapis.com/css2?family=Marcellus&family=PT+Sans:wght@400;700&display=swap">
<style>
  :root {
    --ink: #1f3d4c;
    --tan: #8f8771;
    --paper: #ffffff;
    --line: #2c4552;
    --stage: #e9e6e0;
  }
  * { box-sizing: border-box; margin: 0; padding: 0; }
  html, body { width: 1200px; height: 1024px; overflow: hidden; }
  body {
    background: var(--stage);
    font-family: "PT Sans", Arial, sans-serif;
    position: relative;
  }
  .card {
    position: absolute;
    width: 700px;
    height: 400px;
    background: var(--paper);
    box-shadow: 0 6px 18px rgba(0,0,0,.18);
    overflow: hidden;
  }
  .card--appointment { left: 60px; top: 80px; }
  .card--business { left: 440px; top: 544px; display: flex; }

  /* brand lockup */
  .brand {
    display: flex;
    flex-direction: column;
    align-items: center;
    text-align: center;
  }
  .brand__dot {
    width: 120px; height: 120px;
    border-radius: 50%;
    background: var(--tan);
    margin-bottom: 18px;
  }
  .brand__name {
    font-family: "Marcellus", Georgia, serif;
    color: var(--ink);
    font-size: 21px;
    letter-spacing: 2px;
    text-transform: uppercase;
    line-height: 1.3;
  }
  .brand__tagline {
    margin-top: 10px;
    font-size: 15px;
    font-weight: 700;
    color: var(--ink);
  }
  .brand__label {
    margin-top: 10px;
    font-family: "Marcellus", Georgia, serif;
    font-size: 26px;
    letter-spacing: 2px;
    color: var(--ink);
  }

  /* appointment side */
  .card--appointment .brand {
    position: absolute; left: 40px; top: 70px; width: 280px;
  }
  .appointment-fields {
    position: absolute; left: 340px; top: 80px; right: 40px;
  }
  .field {
    height: 62px;
    border-bottom: 1.5px solid var(--line);
    display: flex; align-items: flex-end; padding-bottom: 6px;
  }
  .field:first-child { border-bottom-color: var(--tan); }
  .field__label {
    font-family: "Marcellus", Georgia, serif;
    color: var(--tan);
    font-size: 18px;
  }

  /* business side */
  .business__brand-panel {
    width: 44%;
    display: flex; align-items: center; justify-content: center;
    padding: 30px;
  }
  .business__contact-panel {
    width: 56%;
    background: var(--ink);
    color: var(--paper);
    padding: 44px 40px;
    display: flex; flex-direction: column;
  }
  .person__name {
    font-family: "Marcellus", Georgia, serif;
    font-weight: 400;
    font-size: 24px;
    letter-spacing: 1.5px;
    text-transform: uppercase;
  }
  .person__title {
    font-family: "Marcellus", Georgia, serif;
    color: var(--tan);
    font-size: 17px;
    letter-spacing: 1px;
    margin-top: 2px;
  }
  .contact-list { list-style: none; margin-top: 22px; font-size: 16px; line-height: 1.55; }
  .address { margin-top: auto; font-size: 16px; line-height: 1.45; font-style: normal; }
  .address__company {
    font-family: "Marcellus", Georgia, serif;
    color: var(--tan);
    text-transform: uppercase;
    letter-spacing: 1px;
  }
</style>
</head>
<body>

<section class="card card--appointment" aria-label="Appointment card">
  <div class="brand">
    <span class="brand__dot" aria-hidden="true"></span>
    <span class="brand__name">Creekbend Veterinary Services</span>
    <span class="brand__label">APPOINTMENT</span>
  </div>
  <div class="appointment-fields">
    <div class="field"><span class="field__label">Patient's Name:</span></div>
    <div class="field"></div>
    <div class="field"></div>
    <div class="field"></div>
  </div>
</section>

<section class="card card--business" aria-label="Business card">
  <div class="business__brand-panel">
    <div class="brand">
      <span class="brand__dot" aria-hidden="true"></span>
      <span class="brand__name">Creekbend Veterinary Services</span>
      <span class="brand__tagline">Patients First, Every Visit</span>
    </div>
  </div>
  <div class="business__contact-panel">
    <h1 class="person__name">Dr. Freya L Tovell</h1>
    <p class="person__title">BVSC (HONS)</p>
    <ul class="contact-list">
      <li>P: 0741872306 / 0418365947</li>
      <li>F: 0741872309</li>
      <li>E: creekbendvets@mailnest.example</li>
    </ul>
    <address class="address">
      <span class="address__company">Creekbend Veterinary Services</span><br>
      17 Harrow St Wattlegrove,<br>
      QLD 4699
    </address>
  </div>
</section>

</body>
</html>
```